Luxury Business Card Design

We need a business card design for a law firm that look sophisticated and luxury

Target Market(s)

Australian legal markets

Industry/Entity Type

Legal

Contact Information for Business Card

Attached

Requirements
Must have
• Logo, head office address on front side and 2 other addresses on the back side.
Nice to have
• Please see below our current business card. Need something more sophisticated and luxury feel

```html
<!DOCTYPE html>
<html lang="en">
<head>
<meta charset="utf-8">
<title>Harrowgate Lawyers – Business Card</title>
<link href="https://fonts.googleapis.com/css2?family=Tinos:wght@400;700&display=swap" rel="stylesheet">
<style>
  :root{
    --bg:#232323;
    --green:#0b1e12;
    --green-soft:#2a4630;
    --gold:#d1a961;
    --ink:#0f2016;
    --white:#ffffff;
  }
  *{box-sizing:border-box;margin:0;padding:0}
  html,body{width:1200px;height:780px;overflow:hidden;background:var(--bg)}
  body{position:relative;font-family:"Tinos","Times New Roman",serif;color:var(--ink)}

  .card{position:absolute;border-radius:22px;overflow:hidden}

  /* Back side */
  .card-back{left:70px;top:225px;width:570px;height:330px;background:var(--green)}
  .office-band{display:flex;height:128px;background:var(--gold)}
  .office{flex:1;padding:16px 22px;font-size:13px;line-height:1.35;color:var(--ink)}
  .office-divider{width:8px;background:var(--green)}
  .office-city{font-weight:700;font-size:14px;letter-spacing:.5px;margin-bottom:3px}
  .office-phone{display:flex;align-items:center;gap:6px;margin-top:3px}
  .office-phone svg{width:14px;height:14px}
  .tagline{margin-top:16px;text-align:center;color:var(--gold);font-size:13px;letter-spacing:2.5px}
  .tagline .sep{display:inline-block;width:6px;height:6px;border-radius:50%;background:var(--gold);margin:0 10px;vertical-align:middle}
  .back-brand{display:flex;align-items:center;justify-content:center;gap:18px;margin-top:40px;padding:0 30px}
  .back-brand .brand-circle{flex:none;width:62px;height:62px;border-radius:50%;border:3px solid var(--green-soft)}
  .back-brand .brand-name{font-weight:700;font-size:28px;letter-spacing:2px;color:var(--green-soft);white-space:nowrap}

  /* Front side */
  .card-front{left:760px;top:100px;width:340px;height:580px;background:var(--white);padding:28px 30px}
  .front-brand{display:flex;flex-direction:column;align-items:center;gap:12px}
  .front-brand .brand-circle{width:60px;height:60px;border-radius:50%;border:3px solid var(--gold)}
  .front-brand .brand-name{font-weight:700;font-size:21px;line-height:1.25;letter-spacing:1.5px;color:var(--ink);text-align:center}

  .person{margin-top:40px;text-align:center}
  .person-name{font-size:30px;font-weight:700;letter-spacing:1px;line-height:1.2}
  .person-name .first{color:var(--gold)}
  .person-role{font-size:13px;letter-spacing:.6px;margin-top:4px}
  .person-degree{font-size:12px;margin-top:2px}

  .rule{height:2px;margin:11px 0;background:linear-gradient(90deg,transparent,var(--gold) 30%,var(--gold) 70%,transparent)}
  .icon-row{display:flex;justify-content:center;gap:8px;margin-top:12px}
  .icon{width:26px;height:26px;border-radius:50%;background:var(--gold);display:flex;align-items:center;justify-content:center}
  .icon svg{width:14px;height:14px}
  .contacts{text-align:center;font-size:14px;line-height:1.38}
  .address{text-align:center;font-size:14px;line-height:1.38;margin-top:6px}
  .rule-end{margin-bottom:0}
</style>
</head>
<body>

<section class="card card-back" aria-label="Business card, back side">
  <div class="office-band">
    <div class="office">
      <div class="office-city">PERTH</div>
      <div>Suite 12, 40 Marlow Highway</div>
      <div>NEDLANDS WA 6009</div>
      <div class="office-phone">
        <svg viewBox="0 0 16 16"><circle cx="8" cy="8" r="8" fill="#0f2016"/><path d="M5.2 4.3l1.4-.3.8 1.9-.9.7a5 5 0 0 0 2.9 2.9l.7-.9 1.9.8-.3 1.4c-3.6.3-6.8-2.9-6.5-6.5z" fill="#d1a961"/></svg>
        +61 08 6000 5128
      </div>
    </div>
    <div class="office-divider"></div>
    <div class="office">
      <div class="office-city">MELBOURNE</div>
      <div>Suite 310, Ashby Chambers 215 Little</div>
      <div>Lonsdale Street MELBOURNE VIC 3000</div>
      <div class="office-phone">
        <svg viewBox="0 0 16 16"><circle cx="8" cy="8" r="8" fill="#0f2016"/><path d="M5.2 4.3l1.4-.3.8 1.9-.9.7a5 5 0 0 0 2.9 2.9l.7-.9 1.9.8-.3 1.4c-3.6.3-6.8-2.9-6.5-6.5z" fill="#d1a961"/></svg>
        +61 03 9000 3361
      </div>
    </div>
  </div>
  <p class="tagline">YOUR SOLUTION<span class="sep"></span>YOUR SUCCESS<span class="sep"></span>IT MATTERS</p>
  <div class="back-brand">
    <span class="brand-circle"></span>
    <span class="brand-name">HARROWGATE LAWYERS</span>
  </div>
</section>

<section class="card card-front" aria-label="Business card, front side">
  <div class="front-brand">
    <span class="brand-circle"></span>
    <span class="brand-name">HARROWGATE<br>LAWYERS</span>
  </div>

  <div class="person">
    <div class="person-name"><span class="first">DANIEL</span> MERCER</div>
    <div class="person-role">DIRECTOR &amp; PRINCIPAL SOLICITOR</div>
    <div class="person-degree">MBA, Juris Doctor</div>
  </div>

  <div class="icon-row">
    <span class="icon"><svg viewBox="0 0 16 16"><path d="M3.5 2.5l2.3-.5 1.2 3-1.4 1.1a8 8 0 0 0 4.3 4.3l1.1-1.4 3 1.2-.5 2.3C7.8 13 3 8.2 3.5 2.5z" fill="#fff"/></svg></span>
    <span class="icon"><svg viewBox="0 0 16 16"><rect x="2" y="4" width="12" height="8" rx="1" fill="none" stroke="#fff" stroke-width="1.4"/><path d="M2.5 4.5L8 9l5.5-4.5" fill="none" stroke="#fff" stroke-width="1.4"/></svg></span>
    <span class="icon"><svg viewBox="0 0 16 16"><circle cx="8" cy="8" r="5.5" fill="none" stroke="#fff" stroke-width="1.3"/><ellipse cx="8" cy="8" rx="2.4" ry="5.5" fill="none" stroke="#fff" stroke-width="1.1"/><path d="M2.5 8h11" stroke="#fff" stroke-width="1.1"/></svg></span>
  </div>
  <div class="rule"></div>
  <div class="contacts">
    <div>+61 7 3000 4182 (Office)</div>
    <div>+61 0400 000 271 (Mobile)</div>
    <div>www.harrowgatelawyers.com.au</div>
    <div>daniel@harrowgatelawyers.com.au</div>
  </div>
  <div class="rule"></div>
  <div class="icon-row">
    <span class="icon"><svg viewBox="0 0 16 16"><path d="M8 14s-4.5-4.6-4.5-8a4.5 4.5 0 0 1 9 0c0 3.4-4.5 8-4.5 8z" fill="#fff"/><circle cx="8" cy="6" r="1.7" fill="#d1a961"/></svg></span>
  </div>
  <div class="address">
    <div>Level 3, Harrowgate House,</div>
    <div>120 Ashworth Terrace,</div>
    <div>Kelvin Grove, QLD 4059</div>
  </div>
  <div class="rule rule-end"></div>
</section>

</body>
</html>
```